Email Signature

We would like to have an email Signature designed.
We have an idea, and a logo that we would like to be make more professional in design and look.

```html
<!DOCTYPE html>
<html lang="en">
<head>
<meta charset="utf-8">
<title>Email Signature – Sam Whitford</title>
<link rel="stylesheet" href="https://fonts.googleapis.com/css2?family=Crimson+Pro:wght@400&family=Source+Sans+3:wght@400;600&display=swap">
<style>
  :root {
    --page-bg: #ffffff;
    --card-bg: #ffffff;
    --ink-dark: #2b2f33;
    --brand-blue: #2684ff;
    --brand-orange: #ff3b14;
    --panel-grey: #d0d9d7;
    --shadow: rgba(0, 0, 0, 0.35);
  }
  * { margin: 0; padding: 0; box-sizing: border-box; }
  html, body {
    width: 1200px;
    height: 631px;
    overflow: hidden;
    background: var(--page-bg);
  }
  .canvas {
    position: relative;
    width: 1200px;
    height: 631px;
  }
  .signature {
    position: absolute;
    left: 96px;
    top: 196px;
    width: 1040px;
    height: 238px;
    background: var(--card-bg);
    box-shadow: 4px 6px 12px var(--shadow);
    overflow: hidden;
  }
  .signature__shapes {
    position: absolute;
    inset: 0;
    width: 100%;
    height: 100%;
  }
  .panel-grey { fill: var(--panel-grey); }
  .bar-blue { fill: var(--brand-blue); }
  .bar-orange { fill: var(--brand-orange); }

  .person {
    position: absolute;
    left: 26px;
    top: 36px;
  }
  .person__name {
    font-family: "Crimson Pro", Georgia, serif;
    font-weight: 400;
    font-size: 29px;
    line-height: 1;
    color: var(--ink-dark);
  }
  .person__role {
    margin-top: 4px;
    font-family: "Source Sans 3", Arial, sans-serif;
    font-weight: 400;
    font-size: 19px;
    line-height: 1.1;
    color: var(--brand-blue);
  }
  .contact {
    position: absolute;
    left: 26px;
    top: 132px;
    font-family: "Source Sans 3", Arial, sans-serif;
    font-size: 16px;
    line-height: 1;
    color: var(--brand-blue);
  }
  .contact__label { margin-right: 6px; }

  .company {
    position: absolute;
    right: 44px;
    top: 148px;
    display: flex;
    align-items: center;
    gap: 10px;
  }
  .company__dot {
    width: 30px;
    height: 30px;
    border-radius: 50%;
    background: var(--brand-orange);
  }
  .company__name {
    font-family: "Source Sans 3", Arial, sans-serif;
    font-weight: 600;
    font-size: 30px;
    line-height: 1;
    color: var(--brand-blue);
  }
</style>
</head>
<body>
<div class="canvas">
  <div class="signature">
    <svg class="signature__shapes" viewBox="0 0 1040 238" aria-hidden="true">
      <polygon class="panel-grey" points="640,238 760,110 1040,110 1040,238"/>
      <rect class="bar-blue" x="0" y="228" width="200" height="10"/>
      <rect class="bar-orange" x="200" y="228" width="120" height="10"/>
    </svg>

    <div class="person">
      <p class="person__name">Sam Whitford</p>
      <p class="person__role">Client Relation</p>
    </div>

    <p class="contact"><span class="contact__label">M:</span>+6140012345678</p>

    <div class="company">
      <span class="company__dot"></span>
      <span class="company__name">Tenfold Advisory</span>
    </div>
  </div>
</div>
</body>
</html>
```